Sidebar ad for rare disease patient registries

We have a product (ENGAGE) that allows patient advocacy foundations to promote our patient registries while maintaining their own branding. We need a sidebar ad and banner ad designed that we could provide to the advocacy organizations to post on their own websites. The advocacy groups get a unique URL from us and they promote this URL to their disease community. When a user clicks the link, we change the branding on our site to reflect the advocacy organization's branding.

Having the ability to have a quality graphical ad on their foundation webpages that entice their patient community to join our registries is be critical. Looking for something about 230 px wide by 500 px tall.

We would provide multiple different text messages on the ads, so need room to have a headline and maybe a short sentence and a button that users would push to 'ENGAGE' to join the patient registry.

Would like a stylized button with the word ENGAGE on it which would take the user to our registry. Possibly include the caremeadowline logo in the button / graphic somehow in a tasteful way. CareMeadowline operates the technology and registry program, but we don't want to overtly brand ourselves but would like to include our brand if possible. We can not get between the advocacy organizations and the patient community. This is very much about trust with the patient community and asking them to share detailed medical history. They will not be sharing their information with CareMeadowline, but rather the advocacy organization that will have this ad on their website.

Would eventually like a series of graphics that an advocacy organization could choose from.

Example tag lines:

Give future generations a precious gift: your medical information

Give the global patient community the gift of your participation

Help researchers to help patients: Participate in trials and studies

Help researchers help you: Join our patient registry

The more researchers know about patients, the sooner they can find answers

Joining the patient registry helps the global patient community

Make your medical information count! Join the [your disease] registry

Pharma can’t invest in research if they don’t know how many patients have [your disease]. Help us build our patient registry.

There’s power in numbers. Help us build our patient registry.

Why participate in the [your disease] registry? Raise the visibility of [your disease] and generate more research interest.

FYI, our logo can be found at http://www.caremeadowline-example.com/templates/ja_social/images/logo.png

Also, we would prefer images that reflect patients as opposed to healthcare professionals if possible and please mention the words Patient Registry in the text.

Target Market(s)

Disease foundations and patient advocacy organizations. For example:
http://www.renalhopealliance-example.org
http://www.ifacepressure-example.com/
http://www.milosfreshstart-example.org
http://www.familyeffortnm-example.org
http://www.musclefadeunion-example.org

Industry/Entity Type

Product

```html
<!DOCTYPE html>
<html lang="en">
<head>
<meta charset="utf-8">
<title>CareMeadowline – Patient Registry Sidebar Ad</title>
<link rel="stylesheet" href="https://fonts.googleapis.com/css2?family=Arimo:wght@400&family=Cabin:wght@500&family=Patrick+Hand&display=swap">
<style>
  :root {
    --stage: #4a4f55;
    --paper: #ffffff;
    --linen: #eeeeee;
    --brand-blue: #3d8fd9;
    --logo-blue: #3a7fc1;
    --leaf-green: #6aab2a;
    --leaf-green-dark: #4e8d1c;
    --ink: #3b3b3b;
    --photo-light: #e9ecef;
    --photo-mid: #b9c0c7;
  }
  * { box-sizing: border-box; margin: 0; padding: 0; }
  html, body {
    width: 1200px;
    height: 900px;
    overflow: hidden;
    background: var(--stage);
  }
  .sidebar-ad {
    position: absolute;
    left: 427px;
    top: 75px;
    width: 345px;
    height: 750px;
    background: linear-gradient(180deg, var(--linen) 0%, #f3f3f3 100%);
    overflow: hidden;
  }
  .brand-bar {
    position: absolute;
    left: 0; top: 0;
    width: 100%;
    height: 72px;
    background: var(--paper);
    display: flex;
    align-items: center;
    gap: 10px;
    padding-left: 9px;
    z-index: 2;
  }
  .brand-dot {
    width: 30px; height: 30px;
    border-radius: 50%;
    background: var(--logo-blue);
  }
  .brand-name {
    font-family: "Arimo", sans-serif;
    font-weight: 400;
    font-size: 23px;
    letter-spacing: 1.5px;
    color: var(--logo-blue);
  }
  .hero-photo {
    position: absolute;
    left: 0; top: 72px;
    width: 100%;
    height: 336px;
    background: linear-gradient(180deg, var(--photo-mid) 0%, var(--photo-light) 60%, var(--linen) 100%);
  }
  .swoosh {
    position: absolute;
    left: 0; top: 55px;
    width: 345px;
    height: 60px;
    z-index: 3;
  }
  .headline {
    position: absolute;
    left: 20px;
    top: 398px;
    font-family: "Arimo", sans-serif;
    font-weight: 400;
    font-size: 43px;
    line-height: 53px;
    color: var(--brand-blue);
    letter-spacing: -0.5px;
  }
  .subline {
    position: absolute;
    left: 20px;
    top: 558px;
    font-family: "Patrick Hand", cursive;
    font-size: 29px;
    color: var(--ink);
  }
  .engage-button {
    position: absolute;
    left: 37px;
    top: 625px;
    width: 266px;
    height: 70px;
    display: block;
    text-decoration: none;
  }
  .engage-button svg { position: absolute; inset: 0; }
  .engage-label {
    position: absolute;
    left: 76px;
    top: 0;
    height: 70px;
    line-height: 70px;
    font-family: "Cabin", sans-serif;
    font-weight: 500;
    font-size: 28px;
    letter-spacing: 1px;
    color: var(--paper);
  }
</style>
</head>
<body>
  <aside class="sidebar-ad">
    <header class="brand-bar">
      <span class="brand-dot"></span>
      <span class="brand-name">CareMeadowline</span>
    </header>

    <div class="hero-photo" role="img" aria-label="Photo of medical lab results with a pen and stethoscope"></div>

    <svg class="swoosh" viewBox="0 0 345 60" aria-hidden="true">
      <path d="M0 0 H345 V45 C250 12 110 4 0 17 Z" fill="#ffffff"/>
      <path d="M0 17 C110 4 250 12 345 45 L345 54 C250 20 110 13 0 26 Z" fill="var(--leaf-green)"/>
    </svg>

    <h1 class="headline">Give future<br>generations<br>a precious gift</h1>
    <p class="subline">your medical information</p>

    <a class="engage-button" href="#">
      <svg viewBox="0 0 266 70" aria-hidden="true">
        <path d="M8 4 H232 L264 35 L232 66 H8 Z" fill="var(--leaf-green)"/>
        <path d="M8 50 H248 L232 66 H8 Z" fill="var(--leaf-green-dark)" opacity="0.35"/>
        <circle cx="30" cy="35" r="26" fill="#ffffff"/>
      </svg>
      <span class="engage-label">ENGAGE</span>
    </a>
  </aside>
</body>
</html>
```